Bref créative
quenzol stationary design
Stationary design
Modern
Ling Paoshen
Manager
52/3F Tanshu Road, Taipei,Taiwan
ling@quenzol.com
quenzol.com
I will like to have 12 sheeps jumping around and the design can derive from my logo. We can have characters such as 1: happy / laughing, 2: surprissed, 3: angry, 5: mysterious, 6: hurry and impatient, 7: affraid / chicken-hearted; cowardly, 8: Strong and muscular,
9: brave. Personalities that are fun .
Jumping sheeps

```html
<!DOCTYPE html>
<html lang="en">
<head>
<meta charset="utf-8">
<title>quenzol stationery</title>
<link href="https://fonts.googleapis.com/css2?family=Open+Sans:wght@400;600;700&display=swap" rel="stylesheet">
<style>
:root{
  --backdrop:#b0662f;
  --navy:#2c3f66;
  --paper:#ffffff;
  --ink:#4a4f5c;
  --rule:#b9bfcc;
  --faint:#eceef2;
}
*{box-sizing:border-box;margin:0;padding:0}
html,body{width:1200px;height:566px;overflow:hidden}
body{background:var(--backdrop);font-family:"Open Sans",sans-serif;color:var(--ink);position:relative}
.sheet{position:absolute;background:var(--paper);box-shadow:0 2px 6px rgba(0,0,0,.3);overflow:hidden}
.band{position:absolute;left:0;right:0;background:var(--navy);color:#fff}
.brand{display:flex;align-items:center;gap:5px;font-weight:700;color:#fff;white-space:nowrap}
.brand .dot{border-radius:50%;background:#fff;flex:none}
.tiny{font-size:4px;line-height:1.5;color:#fff}
.label{position:absolute;color:#fff;font-size:20px;font-weight:400;top:486px}

/* letterhead */
.letterhead{left:115px;top:48px;width:236px;height:422px}
.letterhead .band.top{top:0;height:30px;display:flex;align-items:center;justify-content:center}
.letterhead .band.top .brand{font-size:13px}
.letterhead .band.top .brand .dot{width:14px;height:14px}
.letterhead .band.top .tiny{position:absolute;right:8px;top:6px;text-align:right}
.letterhead .band.bottom{bottom:0;height:12px;display:flex;align-items:center;justify-content:center;gap:10px}
.watermark{position:absolute;display:flex;flex-direction:column;align-items:center;color:var(--faint);font-weight:700}
.watermark .circle{border-radius:50%;background:var(--faint)}
.letterhead .watermark{left:0;right:0;top:80px;font-size:46px}
.letterhead .watermark .circle{width:110px;height:110px;margin-bottom:4px}

/* fax */
.fax{left:403px;top:48px;width:293px;height:422px}
.fax .band.top{top:0;height:30px;display:flex;align-items:center;justify-content:center}
.fax .band.top .brand{font-size:13px}
.fax .band.top .brand .dot{width:14px;height:14px}
.fax .band.top .tiny{position:absolute;right:8px;top:6px;text-align:right}
.fax h1{position:absolute;left:20px;top:62px;font-size:20px;font-weight:600;color:#333}
.fax-fields{position:absolute;left:20px;right:20px;top:92px;display:grid;grid-template-columns:1fr 1fr;column-gap:18px;row-gap:7px}
.field{font-size:5px;border-bottom:1px solid var(--rule);padding-bottom:1px;color:#666}
.fax .divider{position:absolute;left:20px;right:20px;top:146px;border-top:1px solid var(--rule)}
.checks{position:absolute;left:20px;right:20px;top:154px;display:flex;justify-content:space-between;font-size:5px;color:#555}
.checks span::before{content:"";display:inline-block;width:5px;height:5px;border:1px solid #888;margin-right:3px;vertical-align:-1px}
.fax .watermark{right:40px;bottom:30px;font-size:18px}
.fax .watermark .circle{width:40px;height:40px;margin-bottom:2px}

/* envelopes */
.envelope-back{left:749px;top:48px;width:374px;height:144px}
.envelope-back svg{position:absolute;left:0;top:0}
.envelope-back .brand{position:absolute;left:0;right:0;top:14px;justify-content:center;font-size:11px}
.envelope-back .brand .dot{width:12px;height:12px}
.envelope-front{left:749px;top:180px;width:374px;height:180px}
.envelope-front .band{top:0;height:42px}
.envelope-front .band .brand{position:absolute;right:20px;top:12px;font-size:13px}
.envelope-front .band .brand .dot{width:14px;height:14px}
.envelope-front .return{position:absolute;left:18px;top:48px;font-size:5px;color:#555}
.envelope-front .web{position:absolute;left:18px;bottom:10px;font-size:5px;color:#555}

/* cards */
.card{width:135px;height:53px}
.card-name{left:763px;top:384px}
.card-name .who{position:absolute;left:8px;top:6px;font-size:5px;color:#333}
.card-name .who b{font-weight:700;margin-right:4px}
.card-name .band{top:21px;height:24px;display:flex;align-items:center;justify-content:flex-end;padding-right:8px}
.card-name .brand{font-size:9px}
.card-name .brand .dot{width:9px;height:9px}
.card-back{left:922px;top:384px}
.card-back .band{top:10px;height:33px;display:flex;align-items:center;justify-content:flex-end;padding-right:10px}
.card-back .brand{font-size:11px}
.card-back .brand .dot{width:11px;height:11px}
.card-plain{left:869px;top:468px;height:50px}
.card-plain .brand{position:absolute;left:0;right:0;top:16px;justify-content:center;color:var(--navy);font-size:11px}
.card-plain .brand .dot{width:11px;height:11px;background:var(--navy)}
.card-plain .contact{position:absolute;left:8px;bottom:4px;font-size:4px;color:#666}
</style>
</head>
<body>

<section class="sheet letterhead" aria-label="Letterhead">
  <div class="band top">
    <div class="brand"><span class="dot"></span>quenzol</div>
    <div class="tiny">52/3F Tanshu Road<br>Taipei, Taiwan</div>
  </div>
  <div class="watermark" aria-hidden="true"><span class="circle"></span>quenzol</div>
  <div class="band bottom">
    <span class="tiny">Tel +886 2 5550 1478</span>
    <span class="tiny">52/3F Tanshu Road, Taipei, Taiwan</span>
    <span class="tiny">ling@quenzol.com</span>
  </div>
</section>
<div class="label" style="left:236px">Option-1</div>

<section class="sheet fax" aria-label="Fax sheet">
  <div class="band top">
    <div class="brand"><span class="dot"></span>quenzol</div>
    <div class="tiny">52/3F Tanshu Road<br>Taipei, Taiwan</div>
  </div>
  <h1>FAX</h1>
  <div class="fax-fields">
    <div class="field">To:</div><div class="field">From:</div>
    <div class="field">Fax:</div><div class="field">Pages:</div>
    <div class="field">Phone:</div><div class="field">Date:</div>
    <div class="field">Re:</div><div class="field">CC:</div>
  </div>
  <div class="divider"></div>
  <div class="checks">
    <span>Urgent</span><span>For Review</span><span>Please Comment</span><span>Please Reply</span><span>Please Recycle</span>
  </div>
  <div class="watermark" aria-hidden="true"><span class="circle"></span>quenzol</div>
</section>
<div class="label" style="left:512px">Option-2</div>

<section class="sheet envelope-back" aria-label="Envelope back">
  <svg width="374" height="144" viewBox="0 0 374 144">
    <polygon points="0,0 374,0 374,10 187,74 0,10" fill="var(--navy)"/>
  </svg>
  <div class="brand"><span class="dot"></span>quenzol</div>
</section>

<section class="sheet envelope-front" aria-label="Envelope front">
  <div class="band"><div class="brand"><span class="dot"></span>quenzol</div></div>
  <div class="return">52/3F Tanshu Road, Taipei, Taiwan</div>
  <div class="web">quenzol.com</div>
</section>

<section class="sheet card card-name" aria-label="Business card front">
  <div class="who"><b>Ling Paoshen</b>Manager</div>
  <div class="band"><div class="brand"><span class="dot"></span>quenzol</div></div>
</section>

<section class="sheet card card-back" aria-label="Business card back">
  <div class="band"><div class="brand"><span class="dot"></span>quenzol</div></div>
</section>

<section class="sheet card card-plain" aria-label="Business card">
  <div class="brand"><span class="dot"></span>quenzol</div>
  <div class="contact">ling@quenzol.com · quenzol.com</div>
</section>

</body>
</html>
```